Thimble Nook web site

I have been running an online business for 6 years.
www.thimblenook.com.au I specialise in ribbons, buttons and unique craft materials. I sell online to individuals and shops with seperate retail and wholesale sites. The web page I'd like redesigned is my retail site.

It needs a clean, fresh look. I've recently had a new logo designed (thanks pixel harbour!) and want the web site to incorporate the new design and colour scheme of black and white. (new logo attached as a file)

I no longer want the page with the large image www.thimblenook.com.au I want to have the first page as the retail shop homepage.
http://www.thimblenook.com.au/index.php so this page needs to have all the links

I want to the look to be fresh, modern and clear. It needs to be quick to load.

Notes from my IT guru: They need to know that the following tend to remain static with just the content section changing on each page; Header Left column (but different in the cart) right column (if required) footer
Updates

Thanks for your designs. 1/3 of my users use mobile devices so please take that into consideration. I would like the logo to be incorporated into the design and be a prominent feature (most have just used it as a tiny image in the top left corner. I would like it to be larger and more prominent.  thanks                                   

Thanks to all the designers who have submitted. Can you please add  'Boutique craft supplies' near the logo. That is my tag line. Thanks

Target Market(s)

Crafty females of all ages

Industry/Entity Type

Business

Requirements
Must have
• links to;
blog
gallery
chatterloop
snapboardly
wholesale
space for an image which I change approx every 2 weeks
about Thimble Nook
contact
privacy policy
terms and conditions
newsletter sign up
shipping info
product search
Nice to have
• I am not sure if I want product images on the homepage? I have attached a few images.
Should not have
• not too much colour - I hate the green border I have now

```html
<!DOCTYPE html>
<html lang="en">
<head>
<meta charset="utf-8">
<title>Thimble Nook – Boutique craft supplies</title>
<link href="https://fonts.googleapis.com/css2?family=Arimo:ital,wght@0,400;0,700;1,400&display=swap" rel="stylesheet">
<style>
:root{
  --bar:#4a4a4a;
  --header:#353535;
  --header-light:#4a4a4a;
  --ink:#222;
  --muted:#777;
  --soft:#999;
  --panel:#f3f3f3;
  --panel-head:#ececec;
  --line:#dcdcdc;
  --sale:#e01010;
  --white:#fff;
  --dot:#777;
  --washi:#8fd3e2;
  --ribbon:#7a6a58;
  --button:#3d3d3d;
  --stamp:#c9c9c9;
}
*{box-sizing:border-box;margin:0;padding:0}
html,body{width:746px;height:1200px;overflow:hidden;background:var(--white)}
body{font-family:"Arimo",Arial,sans-serif;color:var(--ink);position:relative}
a{color:inherit;text-decoration:none}
.abs{position:absolute}

.top-bar{left:0;top:0;width:746px;height:22px;background:var(--bar);border-bottom:1px solid #2c2c2c}
.top-links{left:360px;top:0;height:22px;display:flex}
.top-links a{color:#ddd;font-size:8px;line-height:22px;padding:0 18px;border-left:1px solid #5c5c5c}
.social-dots{left:612px;top:2px;display:flex;gap:7px}
.social-dots span{width:18px;height:18px;border-radius:50%;display:block;background:var(--dot)}

.site-header{left:0;top:22px;width:746px;height:86px;background:radial-gradient(ellipse at 180px 30px,var(--header-light),var(--header) 45%)}
.brand{left:68px;top:14px;display:flex;align-items:center;gap:8px}
.brand-mark{width:14px;height:14px;border-radius:50%;background:var(--white)}
.brand-name{color:var(--white);font-size:22px;font-weight:700;line-height:1}
.tagline{left:90px;top:44px;color:#bbb;font-size:9px}
.search{left:536px;top:26px;width:144px;height:25px;border-radius:5px;background:#555;color:#aaa;font-size:8px;padding-left:24px;line-height:25px}
.search svg{position:absolute;left:7px;top:6px}
.main-nav{left:360px;top:68px;display:flex;gap:18px}
.main-nav a{color:#ddd;font-size:10px}
.main-nav a.current{color:var(--white)}

.hero{left:68px;top:116px;width:428px;height:228px;border:1px solid var(--line)}
.hero-image{left:5px;top:5px;width:416px;height:170px;background:linear-gradient(160deg,#f3eff8 0%,#c9b3e3 35%,#f2c9d8 55%,#f4ecb0 75%,#e3efe0 100%)}
.hero-thumbs{left:0;top:178px;width:426px;height:48px;display:flex;border-top:1px solid var(--line)}
.thumb{flex:1;display:flex;align-items:center;gap:10px;padding-left:4px;border-right:1px solid var(--line)}
.thumb:last-child{border-right:0}
.thumb-img{width:50px;height:42px}
.thumb-text{font-size:8px;color:var(--muted);text-align:center;width:70px;line-height:1.3}
.thumb-text b{display:block;color:#888}

.panel{background:var(--panel)}
.panel-title{font-size:12px;font-weight:400;color:var(--ink);background:var(--panel-head);padding:10px 7px;height:34px}
.products{left:68px;width:428px;padding-bottom:10px}
.product-grid{display:grid;grid-template-columns:repeat(5,75px);gap:10px 10px;padding:8px 6px 0}
.product{text-align:center}
.product-img{width:75px;height:44px;margin-bottom:6px}
.p-name{font-size:7.5px;color:#333;white-space:nowrap;margin:0 -6px}
.p-sub{font-size:5.5px;font-weight:700;color:var(--soft)}
.p-price{font-size:8px;color:var(--muted)}
.washi{background:linear-gradient(180deg,#e8f4f6,var(--washi))}
.ribbon{background:linear-gradient(180deg,#f1eee9,var(--ribbon))}
.stamp{background:linear-gradient(180deg,#f4f4f4,var(--stamp))}
.buttons{background:linear-gradient(180deg,#fff,var(--button))}

.sales-title,.partners-title{left:68px;font-size:12px;font-weight:400}
.sales-list{left:67px;top:877px;width:430px;display:grid;grid-template-columns:220px 200px;row-gap:10px}
.sale-name{font-size:9px}
.sale-save{font-size:9px;color:var(--sale)}
.partners{left:68px;top:1016px;width:428px;height:60px}
.badge-a{left:4px;top:5px;width:98px;height:50px;background:linear-gradient(180deg,#6a5a55,#e8d6d6)}
.badge-b{left:107px;top:14px;width:72px;height:27px;background:linear-gradient(90deg,#8a5fb8,#4a6fd0)}
.postage{left:68px;top:1092px;width:428px;height:60px;text-align:center;font-size:6.5px;font-weight:700;color:var(--sale);line-height:1.3;padding-top:14px;white-space:nowrap;letter-spacing:-.1px}
.flag{left:6px;top:0}

.side{left:503px;width:177px}
.side-list{list-style:none;padding:4px 8px 0}
.side-list li{font-size:8px;color:#777;border-bottom:1px solid #e3e3e3;padding:4px 0}
.basket{padding:8px 8px;font-size:7px;line-height:1.9}
.basket .red{color:var(--sale);font-weight:700}
.basket .view{color:#888;margin-top:8px;font-weight:700}
.gallery-grid{display:grid;grid-template-columns:75px 75px;gap:6px 10px;padding:8px 7px 0}
.view-all{font-size:7px;color:#888;font-weight:700;padding:10px 8px}
.blog{padding:12px 10px;font-size:8px;font-style:italic;color:var(--muted);line-height:1.5;position:relative;height:135px}
.quote{font-size:20px;font-style:normal;color:#888;line-height:.6;display:block}
.quote.close{text-align:right}
.blog .author{font-style:normal;text-align:right;margin-top:10px;font-size:7px}
.subscribe{padding:10px 8px;font-size:7px;font-weight:700;color:#555}
.email-row{display:flex;align-items:center;gap:10px;margin-top:12px;color:#999}
.email-field{width:133px;height:18px;background:#d6d6d6}
.join-btn{text-align:right;margin-top:9px;color:#111;padding-right:16px}
.social-names{padding:12px 8px;display:flex;flex-direction:column;gap:12px}
.social-names a{font-size:12px;font-weight:400;color:var(--ink);line-height:1;display:flex;align-items:center;gap:7px}
.social-names a::before{content:"";width:10px;height:10px;background:var(--dot);display:block}

.site-footer{left:0;top:1174px;width:746px;height:26px;background:var(--bar);color:#ccc;font-size:7.5px}
.footer-links{left:67px;top:9px;display:flex;gap:12px}
.copyright{right:68px;top:9px}
</style>
</head>
<body>

<div class="top-bar abs">
  <nav class="top-links abs"><a href="#">Thimble Nook Home</a><a href="#">Shop Home</a><a href="#">Basket</a></nav>
  <div class="social-dots abs" aria-label="Social links"><span></span><span></span><span></span></div>
</div>

<header class="site-header abs">
  <a class="brand abs" href="#"><span class="brand-mark"></span><span class="brand-name">Thimble Nook</span></a>
  <div class="tagline abs">Boutique craft supplies</div>
  <div class="search abs">
    <svg width="12" height="12" viewBox="0 0 12 12"><circle cx="5" cy="5" r="3.5" fill="none" stroke="#bbb" stroke-width="1.5"/><line x1="7.5" y1="7.5" x2="11" y2="11" stroke="#bbb" stroke-width="1.5"/></svg>Search
  </div>
  <nav class="main-nav abs"><a class="current" href="#">About Thimble Nook</a><a href="#">Product</a><a href="#">Shipping Info</a><a href="#">Wholesale</a><a href="#">Contact Us</a></nav>
</header>

<section class="hero abs">
  <div class="hero-image abs" role="img" aria-label="Featured photo: coils of pastel gingham ribbon"></div>
  <div class="hero-thumbs abs">
    <div class="thumb"><div class="thumb-img" role="img" aria-label="Gingham ribbon" style="background:linear-gradient(135deg,#e6d7f0,#f3e7a6)"></div><div class="thumb-text"><b>RIBBON-S</b><br>$234.00</div></div>
    <div class="thumb"><div class="thumb-img" role="img" aria-label="Red ribbon roses" style="background:linear-gradient(135deg,#f0e0e0,#8c2233)"></div><div class="thumb-text"><b>RIBBON-M</b>Great Offer Price<br>12% Discount<br>$234.00</div></div>
    <div class="thumb"><div class="thumb-img" role="img" aria-label="Patterned ribbon rolls" style="background:linear-gradient(135deg,#9bbf6a,#e9b35a)"></div><div class="thumb-text"><b>RIBBON-D</b><br>$234.00</div></div>
  </div>
</section>

<section class="products panel abs" style="top:370px">
  <h2 class="panel-title">Latest Products</h2>
  <div class="product-grid">
    <div class="product"><div class="product-img washi" role="img" aria-label="Washi tape roll"></div><div class="p-name">Washi Tape</div><div class="p-sub">Blue Pattern</div><div class="p-price">$3.50</div></div>
    <div class="product"><div class="product-img ribbon" role="img" aria-label="Pleated ribbon"></div><div class="p-name">Pleated Sated Ribbon</div><div class="p-sub">Brown</div><div class="p-price">$4.00</div></div>
    <div class="product"><div class="product-img washi" role="img" aria-label="Washi tape roll"></div><div class="p-name">Washi Tape</div><div class="p-sub">Blue Pattern</div><div class="p-price">$3.50</div></div>
    <div class="product"><div class="product-img ribbon" role="img" aria-label="Pleated ribbon"></div><div class="p-name">Pleated Sated Ribbon</div><div class="p-sub">Brown</div><div class="p-price">$4.00</div></div>
    <div class="product"><div class="product-img washi" role="img" aria-label="Washi tape roll"></div><div class="p-name">Washi Tape</div><div class="p-sub">Blue Pattern</div><div class="p-price">$3.50</div></div>
    <div class="product"><div class="product-img stamp" role="img" aria-label="Bicycle print washi tape"></div><div class="p-name">Washi Tape</div><div class="p-sub">Bicyles</div><div class="p-price">$2.70</div></div>
    <div class="product"><div class="product-img buttons" role="img" aria-label="Black wooden buttons"></div><div class="p-name">Wodden Button</div><div class="p-sub">Medium Black</div><div class="p-price">$5.00</div></div>
  </div>
</section>

<section class="products panel abs" style="top:613px">
  <h2 class="panel-title">Popular Products</h2>
  <div class="product-grid">
    <div class="product"><div class="product-img washi" role="img" aria-label="Washi tape roll"></div><div class="p-name">Washi Tape</div><div class="p-sub">Blue Pattern</div><div class="p-price">$3.50</div></div>
    <div class="product"><div class="product-img ribbon" role="img" aria-label="Pleated ribbon"></div><div class="p-name">Pleated Sated Ribbon</div><div class="p-sub">Brown</div><div class="p-price">$4.00</div></div>
    <div class="product"><div class="product-img washi" role="img" aria-label="Washi tape roll"></div><div class="p-name">Washi Tape</div><div class="p-sub">Blue Pattern</div><div class="p-price">$3.50</div></div>
    <div class="product"><div class="product-img ribbon" role="img" aria-label="Pleated ribbon"></div><div class="p-name">Pleated Sated Ribbon</div><div class="p-sub">Brown</div><div class="p-price">$4.00</div></div>
    <div class="product"><div class="product-img washi" role="img" aria-label="Washi tape roll"></div><div class="p-name">Washi Tape</div><div class="p-sub">Blue Pattern</div><div class="p-price">$3.50</div></div>
    <div class="product"><div class="product-img stamp" role="img" aria-label="Bicycle print washi tape"></div><div class="p-name">Washi Tape</div><div class="p-sub">Bicyles</div><div class="p-price">$2.70</div></div>
    <div class="product"><div class="product-img buttons" role="img" aria-label="Black wooden buttons"></div><div class="p-name">Wodden Button</div><div class="p-sub">Medium Black</div><div class="p-price">$5.00</div></div>
  </div>
</section>

<h2 class="sales-title abs" style="top:851px">Sales Item</h2>
<div class="sales-list abs">
  <div><div class="sale-name">Inkwell &amp; Co clear stamp - flourishes</div><div class="sale-save">Save $16.95</div></div>
  <div><div class="sale-name">Inkwell &amp; Co clear stamp - flourishes</div><div class="sale-save">Save $12.50</div></div>
  <div><div class="sale-name">Inkwell &amp; Co clear stamp - floral expressions</div><div class="sale-save">Save $10.50</div></div>
  <div><div class="sale-name">Petalia masks - 5 pieces 881993</div><div class="sale-save">Save $7.95</div></div>
  <div><div class="sale-name">Marlow Stead punch - pop up cosmos</div><div class="sale-save">Save $7.00</div></div>
</div>

<h2 class="partners-title abs" style="top:994px">Our Partners</h2>
<div class="partners panel abs">
  <div class="badge-a abs" role="img" aria-label="Partner listing badge"></div>
  <div class="badge-b abs" role="img" aria-label="Partner listing badge"></div>
</div>

<div class="postage panel abs">
  <svg class="flag abs" width="16" height="16" viewBox="0 0 16 16"><path d="M0 0H16V16L8 10L0 16Z" fill="#e01010"/></svg>
  Postage rates (within Australia only)<br>
  Orders over $50 - Free postage<br>
  Orders under $50 - $6 postage charge<br>
  NO international postage without prior postage price agreement. Please do not order online if you do not have an Australian address.
</div>

<aside class="side panel abs" style="top:116px;height:134px">
  <h2 class="panel-title">New Products</h2>
  <ul class="side-list"><li>Adhesive</li><li>Buttons</li><li>Card Kits</li><li>Charms</li><li>Clipboard</li></ul>
</aside>

<aside class="side panel abs" style="top:263px;height:109px">
  <h2 class="panel-title">Shopping Basket</h2>
  <div class="basket"><b style="color:#666">Your Shopping Cart is empty</b><br><span class="red">Items In Cart : 0</span><br><span class="red">Total : $0.00</span><div class="view">View Basket &gt;&gt;</div></div>
</aside>

<aside class="side panel abs" style="top:383px;height:241px">
  <h2 class="panel-title">Products Gallery</h2>
  <div class="gallery-grid">
    <div class="product"><div class="product-img washi" role="img" aria-label="Washi tape roll"></div><div class="p-name">Washi Tape</div><div class="p-sub">Blue Pattern</div><div class="p-price">$3.50</div></div>
    <div class="product"><div class="product-img ribbon" role="img" aria-label="Pleated ribbon"></div><div class="p-name">Pleated Sated Ribbon</div><div class="p-sub">Brown</div><div class="p-price">$4.00</div></div>
    <div class="product"><div class="product-img stamp" role="img" aria-label="Bicycle print washi tape"></div><div class="p-name">Washi Tape</div><div class="p-sub">Bicyles</div><div class="p-price">$2.70</div></div>
    <div class="product"><div class="product-img buttons" role="img" aria-label="Black wooden buttons"></div><div class="p-name">Wodden Button</div><div class="p-sub">Medium Black</div><div class="p-price">$5.00</div></div>
  </div>
  <div class="view-all">View All &gt;&gt;</div>
</aside>

<aside class="side panel abs" style="top:640px;height:171px">
  <h2 class="panel-title">Blogs</h2>
  <div class="blog">
    <span class="quote">&ldquo;</span>
    I specialise in ribbons, buttons and unique craft materials. I sell online to individuals and shops with seperate retail and wholesale sites. The web page I'd like redesigned is my retail site.
    <span class="quote close">&rdquo;</span>
    <div class="author">-Admin</div>
  </div>
</aside>

<aside class="side panel abs" style="top:823px;height:107px">
  <h2 class="panel-title">Subscribe</h2>
  <div class="subscribe">Subscribe to our mailing list below:
    <div class="email-row">Email: <span class="email-field"></span></div>
    <div class="join-btn">Join Now !</div>
  </div>
</aside>

<aside class="side panel abs" style="top:943px;height:132px">
  <h2 class="panel-title">Join Us</h2>
  <nav class="social-names"><a href="#">Chatterloop</a><a href="#">Tweetwave</a><a href="#">Snapboardly</a></nav>
</aside>

<footer class="site-footer abs">
  <nav class="footer-links abs"><a href="#">About Thimble Nook</a><span>|</span><a href="#">Contact Thimble Nook</a><span>|</span><a href="#">Privacy Policy</a><span>|</span><a href="#">Terms &amp; Conditions</a></nav>
  <div class="copyright abs">All Right Reserved 2013-14 ThimbleNook</div>
</footer>

</body>
</html>
```